We need a card design for our company Pebble Harbor Services. Our goal is to save people money on their disposal services. For this post card please put our logo in it. Please use these colors Pantone 576c and 418c or green and grey. We are giving you as the designer the opportunity to be creative with any other images. We are looking to have a fun eye catching postcard.
Please write:
Think you are stuck with your trash bill? Think again
We cut your neighbors disposal cost by 40%.

Please put down our information also,
Contact us
800.555.0147
marlene@gravelnook.com
gravelnook.com

```html
<!DOCTYPE html>
<html lang="en">
<head>
<meta charset="utf-8">
<title>Pebble Harbor Services – Postcard</title>
<link rel="stylesheet" href="https://fonts.googleapis.com/css2?family=Roboto+Condensed:wght@400;700&family=Archivo+Black&family=Open+Sans:wght@400;600&display=swap">
<style>
  :root {
    --green: #6f9d4f;
    --green-bright: #7dc242;
    --green-pale: #bfe0a0;
    --grey: #5c5f61;
    --black: #1d1d1d;
    --white: #ffffff;
    --backdrop: #e9ebe6;
    --rule: #a9aca8;
  }
  * { margin: 0; padding: 0; box-sizing: border-box; }
  html, body { width: 1200px; height: 500px; overflow: hidden; }
  body { background: var(--backdrop); position: relative; font-family: "Roboto Condensed", Arial, sans-serif; }

  .card {
    position: absolute; top: 75px; width: 510px; height: 350px;
    background: var(--white); overflow: hidden;
    box-shadow: 0 4px 14px rgba(0,0,0,.18);
  }
  .card--front { left: 50px; }
  .card--back { left: 630px; }
  .card svg.card__art { position: absolute; inset: 0; }

  .headline { position: absolute; left: 0; right: 0; text-align: center; color: var(--white); font-weight: 700; }
  .headline--question { top: 18px; font-size: 23px; }
  .headline--offer { top: 52px; font-size: 31px; line-height: 36px; }

  .photo-slot { position: absolute; left: 0; top: 150px; width: 185px; height: 200px; }

  .brand { position: absolute; left: 255px; top: 238px; display: flex; align-items: center; gap: 9px; }
  .brand__mark { width: 26px; height: 26px; background: var(--grey); }
  .brand__name { font-family: "Open Sans", Arial, sans-serif; font-weight: 600; font-size: 20px; color: var(--green); }

  .contact { position: absolute; color: var(--grey); }
  .contact__label { font-size: 17px; }
  .contact__phone { font-weight: 700; font-size: 21px; color: var(--green); }
  .contact__email { font-family: "Open Sans", Arial, sans-serif; font-size: 11px; }
  .contact__email span { color: var(--green); font-weight: 600; }

  .front-contact { left: 250px; top: 288px; }
  .front-contact .contact__email { margin-top: 4px; padding-left: 14px; }
  .phone-icon { position: absolute; left: 222px; top: 292px; }

  .back-url { position: absolute; left: 24px; top: 16px; font-family: "Archivo Black", Arial, sans-serif; font-size: 19px; color: var(--white); letter-spacing: .5px; }
  .back-contact { left: 24px; top: 52px; color: var(--white); }
  .back-contact .contact__phone { color: var(--white); }
  .back-contact .contact__email span { color: var(--white); }
  .back-contact .contact__email { color: var(--white); margin-top: 2px; }

  .mission { position: absolute; left: 20px; top: 206px; width: 190px; text-align: center; color: var(--green); font-family: "Open Sans", Arial, sans-serif; font-weight: 600; font-size: 17px; line-height: 24px; }
</style>
</head>
<body>

<section class="card card--front">
  <svg class="card__art" width="510" height="350" viewBox="0 0 510 350" aria-hidden="true">
    <path d="M0 0H510V160C410 178 290 222 140 232C80 236 30 228 0 222Z" fill="var(--green)"/>
    <path d="M140 232C290 222 410 178 510 160V172C410 190 300 230 150 240Z" fill="var(--black)"/>
    <path d="M150 240C300 230 410 190 510 172V188C410 204 300 244 165 246Z" fill="var(--green-bright)"/>
  </svg>
  <p class="headline headline--question">Think you are stuck with your trash bill?</p>
  <p class="headline headline--offer">We cut your neighbors<br>disposal cost by 40%</p>

  <div class="photo-slot" role="img" aria-label="Photo of a smiling woman holding a green recycling bag"
       style="background: linear-gradient(135deg, #8a6a4f 0%, #5d7fa6 45%, #8ccc4a 80%, #b6e27a 100%);"></div>

  <div class="brand">
    <span class="brand__mark"></span>
    <span class="brand__name">Pebble Harbor Services</span>
  </div>

  <svg class="phone-icon" width="20" height="30" viewBox="0 0 20 30" aria-hidden="true">
    <rect x="1" y="1" width="18" height="28" rx="3" fill="var(--green-bright)"/>
    <rect x="4" y="5" width="12" height="17" fill="var(--white)"/>
    <circle cx="10" cy="25.5" r="1.6" fill="var(--white)"/>
  </svg>
  <div class="contact front-contact">
    <div><span class="contact__label">Contact us: </span><span class="contact__phone">800.555.0147</span></div>
    <div class="contact__email">Email: <span>marlene@gravelnook.com</span></div>
  </div>
</section>

<section class="card card--back">
  <svg class="card__art" width="510" height="350" viewBox="0 0 510 350" aria-hidden="true">
    <defs>
      <linearGradient id="backWash" x1="0" x2="1" y1="0" y2="0">
        <stop offset="0.3" stop-color="#ffffff"/>
        <stop offset="1" stop-color="var(--green-pale)"/>
      </linearGradient>
    </defs>
    <rect width="510" height="350" fill="url(#backWash)"/>
    <path d="M0 0H355C300 60 220 135 80 150C45 154 20 153 0 150Z" fill="var(--green)"/>
    <path d="M355 0H372C318 70 230 148 90 158C50 161 22 158 0 156V150C20 153 45 154 80 150C220 135 300 60 355 0Z" fill="var(--black)"/>
    <path d="M372 0H392C335 80 240 160 100 166C55 168 25 164 0 162V156C22 158 50 161 90 158C230 148 318 70 372 0Z" fill="var(--green-bright)"/>
    <rect x="380" y="28" width="90" height="96" fill="var(--white)" stroke="var(--grey)" stroke-width="1.5"/>
    <g stroke="var(--rule)" stroke-width="1">
      <line x1="228" y1="204" x2="472" y2="204"/>
      <line x1="228" y1="240" x2="472" y2="240"/>
      <line x1="228" y1="276" x2="472" y2="276"/>
      <line x1="228" y1="312" x2="472" y2="312"/>
    </g>
  </svg>
  <p class="back-url">www.gravelnook.com</p>
  <div class="contact back-contact">
    <div><span class="contact__label">Contact us: </span><span class="contact__phone">800.555.0147</span></div>
    <div class="contact__email">Email: <span>marlene@gravelnook.com</span></div>
  </div>
  <p class="mission">Our goal is to save people money on their disposal services</p>
</section>

</body>
</html>
```